Webdesign für Luxus Mietwagen mit Chauffeure Service
Zielgruppe
Luxus Mietwagen service mit Chauffeure services.
Die Autos bestehen aus schwarzen Van's, Die Sitzmöglichkeiten sind einstellbar, ausziehbar wie als Bett, Kühlschrank, Kaffe/ Tee und Kaltegetränke sind inkl.
Smart TV mit Internet, Zyntrobox, Quorel TV, sind frei nutzbar.
Möglich sind....kopieren, scannen, drucken.....
Lichtdesign ist einstellbar, USB oder Bluetooth sowie 220 V Steckdosen verfügbar....
Diese Autos werden... über die Webseite per automatic booking bestellbar sein sowie über App in ios und Android.
Eine extra Preisliste Seite zum Vergleich mit Tarifliche Taxi Preis... Wäre Sinnvoll.... Sartpreis soll 30€ und km preis 3.-€ Wartezeit... Stunde 60,-€
Dieser Service startet in Essen...
Es soll hauptsächlich Geschäftsleute von Firmen in NRW ansprechen und Hotels sowie Reiseunternehmen.
Alle, die vergnügt Reisen wollen...
Das Logo ist in unterschiedlichen Farben vorbereitet... In Farbe Pink könnte mann für die Preisliste verwenden.... Gold und Silber müsste mann in Kategorien aufteilen... Wichtig ist dass, auch die als App, einfach sein wird ein Mietwagen zu bestellen.
Aufgabenstellung
Einfachheit, Bescheidenheit... Qualitativ ansprechend :)

```html
<!DOCTYPE html>
<html lang="de">
<head>
<meta charset="utf-8">
<title>Noravel Black – Luxus Autovermietung</title>
<link href="https://fonts.googleapis.com/css2?family=Cinzel:wght@400;700&family=Open+Sans:wght@300;400;600&family=Montserrat:wght@700&family=Kaushan+Script&display=swap" rel="stylesheet">
<style>
:root{
  --bar:#f6e3a1;
  --gold:#c9ad57;
  --gold-text:#c4a24a;
  --dark:#0e0e0e;
  --ink:#2a2a2a;
  --muted:#777;
  --grey:#f1f1f1;
  --white:#fff;
}
*{box-sizing:border-box;margin:0;padding:0}
html,body{width:720px;height:1200px;overflow:hidden;background:#fff}
body{font-family:"Open Sans",sans-serif;color:var(--ink)}
.canvas{display:flex;gap:12px;padding:14px 10px;height:1200px}
.col{width:226px;display:flex;flex-direction:column}
.col--mid{padding-top:40px}
/* top bar */
.topbar{height:25px;background:var(--bar);display:flex;align-items:center;justify-content:space-between;padding:0 5px}
.topbar__call{display:flex;align-items:center;gap:4px;text-align:left}
.topbar__small{font-size:5.5px;font-weight:300;line-height:1.1}
.topbar__num{font-size:7px;font-weight:600;line-height:1.1}
/* hero */
.hero{position:relative;height:300px;background:radial-gradient(ellipse at 40% 40%,#2c2c2c,#050505 70%);color:var(--white);text-align:center}
.hero__brand{position:absolute;top:22px;left:0;right:0;display:flex;justify-content:center;align-items:center;gap:5px;font-family:"Cinzel",serif;font-size:11px;letter-spacing:1px}
.hero__brand i{width:9px;height:9px;border:1px solid #fff;border-radius:50%}
.hero__content{position:absolute;top:145px;left:0;right:0;padding:0 8px}
.hero__title{font-family:"Cinzel",serif;font-weight:700;font-size:14.5px;line-height:1}
.hero__sub{font-family:"Cinzel",serif;font-size:7.5px;color:var(--gold);letter-spacing:2px;margin-top:2px}
.hero__text{font-size:4.6px;margin-top:4px;line-height:1.4}
.hero__app{font-family:"Kaushan Script",cursive;color:var(--gold);font-size:6px;margin-top:8px}
.badges{display:flex;justify-content:center;gap:4px;margin-top:4px}
.badge{width:44px;height:12px;background:#000;border:1px solid #555;border-radius:2px}
.hero__arrow{position:absolute;top:160px;width:7px;height:7px;border-top:1px solid #ccc;border-left:1px solid #ccc}
.hero__arrow--l{left:9px;transform:rotate(-45deg)}
.hero__arrow--r{right:9px;transform:rotate(135deg)}
/* booking */
.booking{height:335px;background:var(--gold);padding:10px 17px;color:var(--white)}
.booking__title{font-family:"Cinzel",serif;font-weight:700;font-size:13.5px;color:var(--dark);text-align:center;margin-bottom:12px}
.booking__title span{color:var(--white)}
.field{margin-bottom:12px}
.field label{display:block;font-size:7px;margin-bottom:3px}
.field__input{height:20px;background:var(--white)}
.row{display:flex;gap:9px}
.row .field{flex:1}
.field__input--clock{position:relative}
.field__input--clock::after{content:"";position:absolute;right:5px;top:5px;width:8px;height:8px;border:1px solid #333;border-radius:50%}
.terms{display:flex;align-items:center;gap:5px;font-size:6px;margin:-2px 0 14px}
.terms i{width:7px;height:7px;background:#fff}
.terms u{color:#3a3a3a}
.submit{height:18px;border:1px solid #fff;text-align:center;font-size:7px;line-height:16px}
/* intro */
.intro{height:180px;background:var(--grey);padding:18px 12px;text-align:center}
.heading{font-family:"Cinzel",serif;font-size:11px;color:#444;line-height:1.2}
.intro p{font-size:5.5px;color:#555;line-height:1.75;margin-top:12px}
/* feature cards */
.photo{height:143px;margin:0 2px}
.photo--meet{background:linear-gradient(135deg,#cfc2a8,#5c5046 60%,#3a3430)}
.photo--hands{background:linear-gradient(160deg,#f5f5f5,#b9bcc0 50%,#2f3136)}
.photo--pair{background:linear-gradient(120deg,#e7e3dc,#6a6058 55%,#2d2a28)}
.photo--phone{background:linear-gradient(120deg,#7a6a5e,#b9a89a 55%,#f0e9e4)}
.feature{position:relative;margin:-8px 2px 0;padding:4px 10px 12px 12px;background:var(--white);border-left:2px solid #8a7d6d}
.feature__title{font-family:"Cinzel",serif;font-size:11.5px;color:var(--gold-text);opacity:.8}
.feature p{font-size:5.4px;color:#555;line-height:1.7;margin-top:3px}
.col--mid .feature{margin-bottom:22px}
/* services */
.services{text-align:center;padding-top:8px}
.services .heading{font-size:9.5px}
.services__grid{display:grid;grid-template-columns:repeat(3,1fr);row-gap:18px;margin-top:22px}
.service{font-size:6.5px;color:#444;display:flex;flex-direction:column;align-items:center;gap:5px}
.service svg{width:24px;height:24px}
.btn{display:inline-block;margin-top:20px;background:var(--gold);color:#fff;font-size:6.5px;padding:6px 16px;border-radius:2px}
/* app promo */
.promo{position:relative;height:225px;clip-path:polygon(0 0,100% 0,100% 88%,0 100%)}
.promo .photo{height:100%;margin:0}
.promo__text{position:absolute;left:11px;top:88px;font-size:6.8px;color:#fff;line-height:1.35;width:150px}
.promo .badges{justify-content:flex-start;margin-top:6px}
.promo .badge{width:58px;height:15px}
/* testimonial */
.reviews{background:var(--grey);margin-top:-18px;padding:36px 12px 18px;text-align:center}
.reviews .heading{font-size:11px}
.reviews__sub{font-size:7px;color:#555;margin-top:4px}
.reviews__line{width:96px;height:1px;background:#555;margin:6px auto 0}
.reviews p{font-size:5.8px;color:#888;line-height:1.85;margin-top:18px}
.person{display:flex;align-items:center;justify-content:center;gap:5px;margin-top:14px}
.person__avatar{width:26px;height:26px;border-radius:50%;background:#7b6656}
.person__name{font-size:7px;font-weight:600;text-align:left;color:#333}
.person__role{font-size:4.5px;color:#888}
.pager{display:flex;justify-content:center;gap:18px;margin-top:20px}
.pager i{width:8px;height:8px;border-top:1px solid #999;border-left:1px solid #999}
.pager i:first-child{transform:rotate(-45deg);opacity:.5}
.pager i:last-child{transform:rotate(135deg)}
/* newsletter */
.newsletter{padding:20px 4px 18px;text-align:center}
.newsletter h3{font-weight:300;font-size:8.8px;line-height:1.3;color:#333}
.newsletter__form{display:flex;align-items:center;justify-content:space-between;margin-top:16px;padding:0 16px 0 6px;border-left:1px solid #bbb}
.newsletter__form span{font-size:8.5px}
.newsletter__form b{background:var(--gold);color:#fff;font-size:4.5px;padding:4px 11px;border-radius:3px}
/* footer */
.footer{flex:1;background:var(--dark);border-top:3px solid var(--gold);color:#fff;padding:12px 12px}
.footer__top{display:flex;justify-content:space-between}
.footer h4{font-size:6.8px;font-weight:400;margin-top:10px}
.footer h4:first-child{margin-top:0}
.footer small{display:block;font-size:4.8px;line-height:1.6;margin-top:4px;color:#ddd}
.footer .accent{color:var(--gold)}
.footer__menu li{list-style:none;font-size:5px;color:#999;line-height:2.1}
.news{margin-top:22px;padding-left:2px}
.news__date{font-size:5px}
.news__title{font-family:"Montserrat",sans-serif;color:var(--gold);font-size:9px;line-height:1.05}
.news p{font-size:5px;line-height:1.65;margin-top:5px;width:125px}
.news a{display:block;font-size:4.8px;color:var(--gold);margin-top:6px}
.footer__greet{font-family:"Kaushan Script",cursive;color:var(--gold);font-size:12px;line-height:1.1;margin-top:16px}
.social{display:flex;gap:8px;margin-top:14px}
.social i{width:10px;height:10px;background:#fff;border-radius:50%}
.copy{font-size:4.5px;line-height:1.6;margin-top:12px}
.copy u{color:var(--gold)}
</style>
</head>
<body>
<div class="canvas">

  <section class="col">
    <header class="topbar">
      <svg width="10" height="9" viewBox="0 0 10 9"><rect y="0" width="10" height="1.6" fill="#222"/><rect y="3.7" width="10" height="1.6" fill="#222"/><rect y="7.4" width="10" height="1.6" fill="#222"/></svg>
      <div class="topbar__call">
        <svg width="10" height="10" viewBox="0 0 10 10"><rect width="10" height="10" rx="2" fill="#222"/><path d="M3 2.2l1 .3.4 1.6-.7.6a4 4 0 0 0 1.6 1.6l.6-.7 1.6.4.3 1c-2.6 1-5.8-2.2-4.8-4.8z" fill="#f6e3a1"/></svg>
        <div><div class="topbar__small">Brauchen Sie Hilfe oder Fragen?</div><div class="topbar__num">Anruf +49 201 / 12 345 678</div></div>
      </div>
    </header>
    <div class="hero" role="img" aria-label="Schwarzer Van bei Nacht">
      <div class="hero__brand"><i></i>Noravel Black</div>
      <span class="hero__arrow hero__arrow--l"></span><span class="hero__arrow hero__arrow--r"></span>
      <div class="hero__content">
        <h1 class="hero__title">LUXUS AUTOVERMIETUNG</h1>
        <div class="hero__sub">MIT CHAUFFEURSERVICE</div>
        <p class="hero__text">Die Autos sind aus schwarzen Lieferwagen, die Sitze sind verstellbar, ausziehbar wie ein Bett, Kühlschrank, Kaffee / Tee und kalte Getränke sind inklusive.</p>
        <div class="hero__app">Online Booking App Also Available</div>
        <div class="badges"><span class="badge"></span><span class="badge"></span></div>
      </div>
    </div>
    <form class="booking">
      <h2 class="booking__title">BOOK YOUR <span>CAR NOW!</span></h2>
      <div class="field"><label>Name For Booking</label><div class="field__input"></div></div>
      <div class="field"><label>Contact Number</label><div class="field__input"></div></div>
      <div class="field"><label>Email Address</label><div class="field__input"></div></div>
      <div class="field"><label>Address</label><div class="field__input"></div></div>
      <div class="row">
        <div class="field"><label>Booking Date</label><div class="field__input field__input--clock"></div></div>
        <div class="field"><label>Time</label><div class="field__input field__input--clock"></div></div>
      </div>
      <div class="terms"><i></i>Accept <u>Terms And Condtions</u></div>
      <div class="submit">SUBMIT</div>
    </form>
    <div class="intro">
      <h2 class="heading">WEGE BESTIMMEN<br>ZIELE ERREICHEN</h2>
      <p>Genießen Sie von Noravel Black die extravagante Transfer-Dienstleistung. Noravel Black bietet Ihnen den exklusiven Transferservice innerhalb sowie auch außerhalb von Essen/NRW an. Modifizierte Fahrzeuge für Ihr persönliches Wohlbefinden, mit besonders gepflegtem Erscheinungsbild von schwarzen Van´s und ausgebildete Chauffeure mit persönlichem Service für den Fahrgast ist für uns selbstverständlich.</p>
    </div>
    <div class="photo photo--meet" role="img" aria-label="Geschäftsleute im Gespräch am Laptop"></div>
    <article class="feature">
      <h3 class="feature__title">WIR SIND INNOVATIV</h3>
      <p>Wer einmal unsere Dienstleistungen kennenlernt, weiß dass er bei uns gut aufgehoben ist. Wir sind verlässlich, diskret, pünktlich. Der Kreis unserer treuen Stammkunden erweitert sich von Tag zu Tag, denn auch sie wissen, das Wohlbefinden ihrer Gäste ist auch unser Wohlbefinden. Unser Anspruch ist es, stets ein souveräner und verlässlicher Partner zu sein. Unser umfangreicher Service besteht nicht nur aus qualitativem Transfer, sondern auch die Sicherheit und der Komfort hat für uns höchste Priorität.</p>
    </article>
  </section>

  <section class="col col--mid">
    <div class="photo photo--hands" role="img" aria-label="Händedruck zweier Geschäftsleute"></div>
    <article class="feature">
      <h3 class="feature__title">ERSTE WAHL</h3>
      <p>Noravel Black wird Ihre erste Wahl bei Transferleistungen. Unsere schwarzen Van´s sind so umgerüstet, dass sie alle notwendigen Mittel haben um Ihre eigene persönliches Wohlbefinden selbst zu entscheiden. Eigenes Lichtdesign einstellen, Musik oder Video Anlage frei nutzen. Wifi in Verbindung mit dem Smart TV / Quorel TV / Zyntrobox / Streamora / Vidlane, Druck und Kopier-Möglichkeiten. Für private Endgeräte sind auch Anschlüsse 220 V Steckdose / USB / HDMI vorhanden.</p>
    </article>
    <div class="photo photo--pair" role="img" aria-label="Zwei Geschäftsleute am Fenster"></div>
    <article class="feature">
      <h3 class="feature__title">WIR SIND INNOVATIV</h3>
      <p>Wir sind innovativ und vielseitig. Es ist für jeden etwas dabei, ob historischer Ausflug oder besonderes Erlebnis, Hochzeitsfahrten oder Ihre ganz persönliche Überraschung – Sie können mit uns gemeinsam Ihre persönliche Fahrt planen und umsetzen. Während Ihrer mobilen Zeit können Sie sich entspannt anlehnen, Kaffee oder Tee genießen. Internet surfen, Emails ausdrucken oder einfach nur die Zeit genießen.</p>
    </article>
    <div class="services">
      <h2 class="heading">BEREICH DER DIENSTLEISTUNGEN</h2>
      <div class="services__grid">
        <div class="service"><svg viewBox="0 0 24 24"><path d="M4 6h13v8a4 4 0 0 1-4 4H8a4 4 0 0 1-4-4z" fill="#222"/><path d="M17 8h2a2 2 0 0 1 0 5h-2" fill="none" stroke="#222" stroke-width="1.6"/><rect x="2" y="20" width="18" height="1.6" fill="#222"/></svg>Coffee</div>
        <div class="service"><svg viewBox="0 0 24 24"><path d="M7 3h10l-1 9a4 4 0 0 1-8 0z M12 16v5 M8 21h8" fill="none" stroke="#333" stroke-width="1.2"/></svg>Cold Drinks</div>
        <div class="service"><svg viewBox="0 0 24 24"><rect x="5" y="2" width="14" height="20" rx="1" fill="none" stroke="#333" stroke-width="1.2"/><path d="M5 8h14M8 5h8" stroke="#333" stroke-width="1"/></svg>Refrigerator</div>
        <div class="service"><svg viewBox="0 0 24 24"><path d="M4 9h13v7a5 5 0 0 1-5 5H9a5 5 0 0 1-5-5z M17 11h2a2 2 0 0 1 0 4h-2 M8 3v4 M12 2v5" fill="none" stroke="#222" stroke-width="1.6"/></svg>Tea</div>
        <div class="service"><svg viewBox="0 0 24 24"><rect x="2" y="4" width="20" height="13" fill="none" stroke="#333" stroke-width="1.3"/><path d="M8 21h8M12 17v4" stroke="#333" stroke-width="1.3"/></svg>Smart TV mit Internet</div>
        <div class="service"><svg viewBox="0 0 24 24"><rect x="3" y="8" width="18" height="9" rx="4.5" fill="#222"/><path d="M7 11v3M5.5 12.5h3" stroke="#fff" stroke-width="1"/><circle cx="16" cy="12.5" r="1" fill="#fff"/></svg>Smart TV mit Internet</div>
        <div class="service"><svg viewBox="0 0 24 24"><path d="M8 3h8l3 3v11H8z M5 7v14h10" fill="none" stroke="#333" stroke-width="1.3"/></svg>Copy</div>
        <div class="service"><svg viewBox="0 0 24 24"><rect x="7" y="3" width="10" height="5" fill="none" stroke="#222" stroke-width="1.5"/><rect x="3" y="8" width="18" height="9" rx="1" fill="#222"/><rect x="7" y="14" width="10" height="7" fill="#fff" stroke="#222" stroke-width="1.5"/></svg>Print</div>
        <div class="service"><svg viewBox="0 0 24 24"><path d="M6 2h9l4 4v8H6z" fill="none" stroke="#333" stroke-width="1.2"/><path d="M3 15h18M5 18h14v4H5z" fill="none" stroke="#333" stroke-width="1.2" stroke-dasharray="2 1"/></svg>Scan</div>
        <div class="service"><svg viewBox="0 0 24 24"><circle cx="12" cy="12" r="9" fill="#222"/></svg>Bluetooth</div>
        <div class="service"><svg viewBox="0 0 24 24"><path d="M4 8l4-4 6 6-4 4z M10 14l4-4 6 6-4 4z" fill="none" stroke="#222" stroke-width="1.6"/></svg>Power</div>
      </div>
      <span class="btn">View All Services</span>
    </div>
  </section>

  <section class="col">
    <div class="promo">
      <div class="photo photo--phone" role="img" aria-label="Lächelnde Frau mit Smartphone"></div>
      <div class="promo__text">über die Webseite per automatic booking bestellbar sein sowie über App in ios und Android.
        <div class="badges"><span class="badge"></span><span class="badge"></span></div>
      </div>
    </div>
    <div class="reviews">
      <h2 class="heading">WHAT OUR SATISFIED<br>CUSTOMER SAYS</h2>
      <div class="reviews__sub">Here Are Some Of Our Client Reviews</div>
      <div class="reviews__line"></div>
      <p>Für die Neugestaltung unserer Webseite hat Lindfeld Media hervorragende Arbeit geleistet. Wir sind sehr zufrieden und bekommen durchaus Feedback unserer Kunden. Wir werden auch im Bereich Online Marketing die Dienstleistungen von Lindfeld Media in Anspruch nehmen.</p>
      <div class="person"><span class="person__avatar" role="img" aria-label="Kundenportrait"></span><div><div class="person__name">Jonas Weider</div><div class="person__role">Verkauf &amp; Marketing RADWERK</div></div></div>
      <div class="pager"><i></i><i></i></div>
    </div>
    <div class="newsletter">
      <h3>Abonnieren Sie unseren Newsletter<br>und verpassen Sie keine neuigkeiten mehr</h3>
      <div class="newsletter__form"><span>Ihre E-Mail Address</span><b>Abonnieren</b></div>
    </div>
    <footer class="footer">
      <div class="footer__top">
        <div>
          <h4>Location</h4><small>Your Address will Replace<br>with This Sample Text.</small>
          <h4>Telephone Enquiry</h4><small class="accent">+49 201 / 12 345 678</small>
          <h4>Email Us</h4><small class="accent">info@noravel.example</small>
        </div>
        <div>
          <h4>Main Menu</h4>
          <ul class="footer__menu"><li>Startseite</li><li>Preisliste</li><li>Serviceseite</li><li>Kontakt</li></ul>
        </div>
      </div>
      <div class="news">
        <div class="news__date">June 8, 2018</div>
        <div class="news__title">WHAT IS<br>LATEST NEWS</div>
        <p>Lorem Ipsum is simply dummy text of the printing and typesetting industry. Lorem Ipsum has been the industry's standard dummy text ever since the 1500s, ...</p>
        <a>View All News</a>
      </div>
      <div class="footer__greet">Wir freuen uns auf<br>ihren besuch .</div>
      <div class="social"><i></i><i></i><i></i><i></i></div>
      <div class="copy">Copyrights 2018 All Rights Reserved.<br>Powered By: <u>studiobeispiel.de</u></div>
    </footer>
  </section>

</div>
</body>
</html>
```